Brochure Design for B-to-B software company

This project is for a product brochure in an 11x17 bifold format. The brochure will be a printed on heavy stock that will fold into 4 - 8 ½” x 11” pages. The folded edge will be on the left side. The brochure will be a combination of text and graphics. The completed editable files will be provided to us for further edits when needed. The color palette should complement and not overuse our logo colors.

Target Market(s)

Corporate Brands

Font styles to use
Sans Serif

Colors
cadf82

Requirements
Must have
• Color palette described in attached project overview document

```html
<!DOCTYPE html>
<html lang="en">
<head>
<meta charset="utf-8">
<title>Leafline CRM – B-to-B Sales Channel Brochure</title>
<link rel="stylesheet" href="https://fonts.googleapis.com/css2?family=Jost:ital,wght@0,400;0,500;0,700;0,800;1,400;1,700;1,800&display=swap">
<style>
:root{
  --green:#6bbf2a;
  --green-light:#cadf82;
  --ink:#141414;
  --black:#1b1b1b;
  --paper:#f6f6f4;
  --text:#2b2b2b;
  --muted:#8a8a8a;
  --stage:#d9d9dc;
  --screen-a:#eef3f8;
  --screen-b:#c9d9e8;
}
*{box-sizing:border-box;margin:0;padding:0}
html,body{width:1200px;height:2520px;overflow:hidden}
body{background:var(--stage);font-family:"Jost",sans-serif;color:var(--text);position:relative}
.view{position:absolute;left:0;width:1200px;height:840px}
.view--cover{top:0}.view--inside{top:840px}.view--outside{top:1680px}
.page{position:absolute;background:var(--paper);overflow:hidden;box-shadow:0 18px 40px rgba(0,0,0,.18)}
.abs{position:absolute}

/* cover */
.cover{width:520px;height:673px}
.cover__band{left:0;top:0;width:520px;height:330px;background:var(--black)}
.cover__title{left:30px;top:40px;width:290px;color:#fff;font-weight:800;font-style:italic;font-size:21px;line-height:1.1;text-transform:uppercase;letter-spacing:.4px}
.cover__intro{left:334px;top:38px;width:166px;color:#fff;font-size:9.5px;line-height:1.3}
.cover__intro h3{color:var(--green);font-style:italic;font-weight:800;font-size:11.5px;line-height:1.1;margin-bottom:4px}
.monitor{left:36px;top:205px;width:290px;height:172px;background:#2a2a2a;border-radius:6px;padding:10px}
.monitor__screen{width:100%;height:100%;background:linear-gradient(135deg,var(--screen-a),var(--screen-b));border-radius:2px}
.monitor__stand{left:141px;top:376px;width:80px;height:10px;background:#2a2a2a;border-radius:0 0 4px 4px}
.tablet{left:380px;top:280px;width:84px;height:110px;background:#2a2a2a;border-radius:8px;padding:7px}
.brand{left:30px;top:412px;font-weight:700;font-size:19px;color:var(--green);white-space:nowrap;display:flex;align-items:center;gap:7px}
.brand__dot{width:10px;height:10px;border-radius:50%;background:var(--green)}
.feat{width:146px;font-size:9.8px;line-height:1.3;color:var(--text)}
.feat h4{color:var(--green);font-style:italic;font-weight:800;font-size:12px;line-height:1.1;margin-bottom:4px}
.feat--c1{left:30px;top:462px}
.feat--c2a{left:200px;top:410px}
.feat--c2b{left:200px;top:540px}
.feat--c3a{left:360px;top:410px}
.feat--c3b{left:360px;top:540px}

/* inside spread */
.spread{width:1040px;height:673px;left:80px;top:84px}
.fold{position:absolute;left:519px;top:0;width:2px;height:673px;background:rgba(0,0,0,.12)}
.photo{background:linear-gradient(160deg,#2f4a2a 0%,#5d7a55 45%,#1c2a1a 100%)}
.shot{background:linear-gradient(180deg,#3a97d8 0 6%,var(--screen-a) 6% 100%);border:1px solid #d6dde4}
.box{padding:14px 16px;font-size:10.5px;line-height:1.4}
.box h4{font-style:italic;font-weight:800;font-size:13.5px;line-height:1.1;margin-bottom:6px}
.box--green{background:var(--green);color:#10210a}
.box--green h4{color:#10210a}
.box--black{background:var(--black);color:#e8e8e8}
.box--black h4,.box--black h5{color:var(--green)}
.box h5{font-style:italic;font-weight:800;font-size:11.5px;margin:8px 0 3px;color:#fff}

/* back page */
.plans__head{left:40px;top:34px;width:280px;background:var(--black);color:#fff;font-style:italic;font-weight:800;font-size:22px;line-height:1.05;padding:12px 16px}
.plans__cols{left:262px;top:112px;width:230px;display:grid;grid-template-columns:repeat(3,1fr);font-style:italic;font-weight:700;font-size:11px;color:var(--text);text-align:center;line-height:1.1}
.plans__cols small{display:block;font-weight:400;font-size:9px}
.plans__rows{left:30px;top:150px;width:470px}
.row{display:grid;grid-template-columns:232px repeat(3,1fr);align-items:center;min-height:31px;font-size:8.2px;line-height:1.25}
.row b{display:block;color:var(--green);font-style:italic;font-weight:700;font-size:9.5px}
.tick{text-align:center;color:var(--green);font-weight:700;font-size:12px}
.plans__foot{left:30px;top:612px;width:470px;display:grid;grid-template-columns:232px repeat(3,1fr);font-style:italic;font-size:10px;align-items:end}
.plans__foot .price{text-align:center;font-weight:700}
.foot-brand{font-weight:700;color:var(--green);font-size:11px;font-style:normal}
.foot-contact{font-size:8.5px;color:var(--text);font-style:normal}
</style>
</head>
<body>

<!-- View 1: front cover -->
<section class="view view--cover">
  <div class="page cover" style="left:340px;top:84px">
    <div class="abs cover__band"></div>
    <h1 class="abs cover__title">B-to-B Sales Channel Management for the Cannabis Industry</h1>
    <div class="abs cover__intro">
      <h3>Accelerate Sales Growth and Scale-up Quickly</h3>
      <p>Developing a B-to-B sales channel can dramatically increase sales growth that complements your retail, marketplace and distributor initiatives. The Leafline CRM B-to-B Sales Channel Management Solution is key to managing that growth and differentiating from competitors. Using our configurable and scalable sales portal CRM technology benefits both you and your customers.</p>
    </div>
    <div class="abs monitor"><div class="monitor__screen" role="img" aria-label="Sales portal dashboard shown on a desktop monitor"></div></div>
    <div class="abs monitor__stand"></div>
    <div class="abs tablet"><div class="monitor__screen" role="img" aria-label="Sales portal shown on a tablet"></div></div>
    <div class="abs brand"><span class="brand__dot"></span>Leafline CRM</div>
    <div class="abs feat feat--c1"><h4>Manage Orders Through Fulfillment</h4><p>Manage products, discounts and inventory in easy-to-use dashboards. Manage sales orders using automated workflow rules and notifications. Direct orders to retailer locations. Alert fulfillment teams as orders become ready for shipment.</p></div>
    <div class="abs feat feat--c2a"><h4>Branded Sales and CRM Portal</h4><p>Launch quickly with your branding, products and content. Allow approved retailers to place sales orders and access CoAs, marketing content and videos.</p></div>
    <div class="abs feat feat--c2b"><h4>Grow and Manage Your Retail Sales Channel</h4><p>Manage retailer leads. Manage on-site marketing activities. Manage Co-op marketing programs. Track retailer performance.</p></div>
    <div class="abs feat feat--c3a"><h4>Pipeline and Sales Analytics</h4><p>Track order status and pipeline with performance dashboards. Analyze order and product sales trends. View real-time key performance indicators (KPIs) for retailers.</p></div>
    <div class="abs feat feat--c3b"><h4>Compliance and Tracking</h4><p>Capture and track license status for retailer locations. View audit trail for complete sales history. Make CoAs available for download at any time.</p></div>
  </div>
</section>

<!-- View 2: inside spread -->
<section class="view view--inside">
  <div class="page spread">
    <!-- left page -->
    <div class="abs photo" style="left:0;top:0;width:520px;height:673px" role="img" aria-label="Cannabis leaf resting on paper currency"></div>
    <div class="abs box box--green" style="left:20px;top:20px;width:180px;height:200px"><h4>Branded Sales and CRM Portal</h4><p>Quickly launch a branded sales portal with your products, content and pricing. Approved retailers sign in to place orders, view order history, download CoAs and access marketing content and videos at any time.</p></div>
    <div class="abs box box--green" style="left:230px;top:60px;width:150px;height:120px"><h4>Manage Orders Through Fulfillment</h4><p>Move every order from entry to shipment with clear status at each step.</p></div>
    <div class="abs box box--green" style="left:60px;top:250px;width:190px;height:170px"><h4>Pipeline and Sales Analytics</h4><p>Performance dashboards show order status, pipeline value and product trends. Real-time KPIs for every retailer help your team act quickly on sales opportunities.</p></div>
    <div class="abs shot" style="left:20px;top:440px;width:250px;height:200px" role="img" aria-label="Analytics dashboard screenshot"></div>
    <div class="abs box box--black" style="left:390px;top:150px;width:130px;height:460px">
      <h5>Enter Orders</h5><p>Retailers and your sales team enter orders in a few clicks, with pricing and discounts applied.</p>
      <h5>Manage Order Flow</h5><p>Workflow rules route each order for approval and notify the right people.</p>
      <h5>Support Your Fulfillment Process</h5><p>Fulfillment teams are alerted as orders become ready to ship.</p>
      <h5>Manage Your Products, Discounts and Inventory</h5><p>Set up SKUs, prices and stock alerts in the product dashboard.</p>
    </div>
    <!-- right page -->
    <div class="abs" style="left:520px;top:0;width:520px;height:673px;background:var(--paper)"></div>
    <div class="abs box box--black" style="left:540px;top:30px;width:210px;height:230px"><h4>Compliance and Tracking</h4><p>Comply with state regulations by keeping track of retailer licenses and expiration dates. The license number for each retailer is stored and shown on invoicing. Sales are tracked by retailer and location, providing a quick view of sales history and export for off-line reporting when needed. Upload your CoAs to your sales portal to give retailers the ability to quickly download them at any time.</p></div>
    <div class="abs shot" style="left:770px;top:40px;width:250px;height:170px" role="img" aria-label="License tracking screen"></div>
    <div class="abs shot" style="left:560px;top:280px;width:250px;height:330px" role="img" aria-label="Product definition form screen"></div>
    <div class="abs box box--black" style="left:830px;top:260px;width:190px;height:390px">
      <h4>Grow Your Retail Sales Channel</h4>
      <h5>Manage Retailer Leads to Expand Your Channel</h5><p>Your business development team can track and manage retailer leads and invite them to join your sales channel.</p>
      <h5>Manage On-site Marketing Activities</h5><p>Coordinate in-store events, trainings and sampling with your sales team.</p>
      <h5>Use Co-Marketing Funds to Increase Retailer Sales</h5><p>Manage co-op programs from contract to payment with performance reporting throughout.</p>
    </div>
    <div class="fold"></div>
  </div>
</section>

<!-- View 3: back and front -->
<section class="view view--outside">
  <div class="page spread">
    <!-- back page -->
    <div class="abs plans__head">Select from these three plans</div>
    <div class="abs plans__cols"><span>Startup<small>Up to 20 SKUs</small></span><span>Standard</span><span>Enterprise/ Distributor</span></div>
    <div class="abs plans__rows">
      <div class="row"><span><b>Branded Sales and CRM Portal</b>Your sales portal carries your brand on desktop or tablet.</span><span class="tick">✕</span><span class="tick">✕</span><span class="tick">✕</span></div>
      <div class="row"><span><b>Customer and Location Management</b>Retailers and locations you set up get sign-in details.</span><span class="tick">✕</span><span class="tick">✕</span><span class="tick">✕</span></div>
      <div class="row"><span><b>Full Sales Cycle Order Management</b>Customers and staff enter orders and track them to delivery.</span><span class="tick">✕</span><span class="tick">✕</span><span class="tick">✕</span></div>
      <div class="row"><span><b>Automated Workflow and Notifications</b>Orders move by rules, with alerts when action is needed.</span><span class="tick">✕</span><span class="tick">✕</span><span class="tick">✕</span></div>
      <div class="row"><span><b>Order Fulfillment Management</b>Give your fulfillment team tools to ship orders quickly.</span><span class="tick">✕</span><span class="tick">✕</span><span class="tick">✕</span></div>
      <div class="row"><span><b>Manage Products, Discounts</b>Set up SKUs, prices, images and discount schedules.</span><span class="tick">✕</span><span class="tick">✕</span><span class="tick">✕</span></div>
      <div class="row"><span><b>Inventory Management</b>Track stock with alerts when quantities run low.</span><span class="tick"></span><span class="tick">✕</span><span class="tick">✕</span></div>
      <div class="row"><span><b>Sales Pipeline and Analytics</b>View the pipeline and retailer performance in real time.</span><span class="tick"></span><span class="tick">✕</span><span class="tick">✕</span></div>
      <div class="row"><span><b>Lead Management</b>Track and manage retailer leads to grow your channel.</span><span class="tick"></span><span class="tick">✕</span><span class="tick">✕</span></div>
      <div class="row"><span><b>Marketing Activity and Incentive Management</b>Manage on-site activities and incentive programs.</span><span class="tick"></span><span class="tick">✕</span><span class="tick">✕</span></div>
      <div class="row"><span><b>CoA and Compliance Tracking</b>Upload CoAs and track licensing for every location.</span><span class="tick"></span><span class="tick"></span><span class="tick">✕</span></div>
      <div class="row"><span><b>Include "Top of mind" Messaging</b>Targeted messages on campaigns, events and topics.</span><span class="tick"></span><span class="tick"></span><span class="tick">✕</span></div>
      <div class="row"><span><b>Manage Multiple Brands</b>Run several brands in a single portal.</span><span class="tick"></span><span class="tick"></span><span class="tick">✕</span></div>
    </div>
    <div class="abs plans__foot">
      <span><span class="foot-brand">Leafline CRM</span><br><span class="foot-contact">www.leaflinecrm.com · +1 555-014-2290</span></span>
      <span class="price">$799/month</span><span class="price">$999/month</span><span class="price">Contact Us</span>
    </div>

    <!-- front page -->
    <div class="abs cover" style="left:520px;top:0;width:520px;height:673px">
      <div class="abs cover__band"></div>
      <h1 class="abs cover__title">B-to-B Sales Channel Management for the Cannabis Industry</h1>
      <div class="abs cover__intro">
        <h3>Accelerate Sales Growth and Scale-up Quickly</h3>
        <p>Developing a B-to-B sales channel can dramatically increase sales growth that complements your retail, marketplace and distributor initiatives. The Leafline CRM B-to-B Sales Channel Management Solution is key to managing that growth and differentiating from competitors. Using our configurable and scalable sales portal CRM technology benefits both you and your customers.</p>
      </div>
      <div class="abs monitor"><div class="monitor__screen" role="img" aria-label="Sales portal dashboard shown on a desktop monitor"></div></div>
      <div class="abs monitor__stand"></div>
      <div class="abs tablet"><div class="monitor__screen" role="img" aria-label="Sales portal shown on a tablet"></div></div>
      <div class="abs brand"><span class="brand__dot"></span>Leafline CRM</div>
      <div class="abs feat feat--c1"><h4>Manage Orders Through Fulfillment</h4><p>Manage products, discounts and inventory in easy-to-use dashboards. Manage sales orders using automated workflow rules and notifications. Direct orders to retailer locations. Alert fulfillment teams as orders become ready for shipment.</p></div>
      <div class="abs feat feat--c2a"><h4>Branded Sales and CRM Portal</h4><p>Launch quickly with your branding, products and content. Allow approved retailers to place sales orders and access CoAs, marketing content and videos.</p></div>
      <div class="abs feat feat--c2b"><h4>Grow and Manage Your Retail Sales Channel</h4><p>Manage retailer leads. Manage on-site marketing activities. Manage Co-op marketing programs. Track retailer performance.</p></div>
      <div class="abs feat feat--c3a"><h4>Pipeline and Sales Analytics</h4><p>Track order status and pipeline with performance dashboards. Analyze order and product sales trends. View real-time key performance indicators (KPIs) for retailers.</p></div>
      <div class="abs feat feat--c3b"><h4>Compliance and Tracking</h4><p>Capture and track license status for retailer locations. View audit trail for complete sales history. Make CoAs available for download at any time.</p></div>
    </div>
    <div class="fold"></div>
  </div>
</section>

</body>
</html>
```